Business Card for beauty technology startup

Design Glowmi Business Card for a Beauty, based on the website identity and colors (https://www.glowmi-example.com).
Glowmi is a beauty tech startup that gathers helpful product info for beauty lovers and consumers (such as availability on stores, price range and product reviews) for makeup products. The card design must be young, colorful but clean, and very modern.

Target Market(s)

woman, 15-35

Industry/Entity Type

Cosmetics

Contact Information for Business Card

Full Name, address, phone

Font styles to use
Other font styles liked:
• Advent Pro

Colors
e34297
86cfc6
ffffff
5c5c5c
e8e8e8
e667a6
b2b2b2

Requirements
Must have
• One full colored side with a creative design and another with card info
• Use Color palette: #95C5C5 and/or #D38AA5
• Use fonts: Advent Pro
• Use website identity: https://www.glowmi-example.com
Nice to have
• If needed extra font: Roboto

```html
<!DOCTYPE html>
<html lang="en">
<head>
<meta charset="utf-8">
<title>Glowmi Business Card</title>
<link rel="stylesheet" href="https://fonts.googleapis.com/css2?family=Advent+Pro:wght@300;600&family=Roboto:wght@400&display=swap">
<style>
  :root {
    --backdrop: #e6e6e6;
    --card-pink-top: #cc8199;
    --card-pink-bottom: #b9728e;
    --card-white: #fbfbfb;
    --ink-dark: #2e2e2e;
    --brand-pink: #c57a98;
    --brand-teal: #7fc3bf;
    --shadow: rgba(0, 0, 0, 0.22);
  }
  html, body {
    margin: 0;
    padding: 0;
    width: 1200px;
    height: 576px;
    overflow: hidden;
    background: var(--backdrop);
  }
  .stage {
    position: relative;
    width: 1200px;
    height: 576px;
  }
  .card {
    position: absolute;
    top: 138px;
    height: 294px;
    border-radius: 14px;
    box-shadow: 2px 4px 8px var(--shadow);
    overflow: hidden;
  }
  .card--front {
    left: 82px;
    width: 485px;
    background: linear-gradient(180deg, var(--card-pink-top) 0%, var(--card-pink-bottom) 100%);
  }
  .card--back {
    left: 602px;
    width: 481px;
    background: var(--card-white);
  }
  .wordmark {
    position: absolute;
    display: flex;
    align-items: center;
    font-family: "Advent Pro", sans-serif;
    font-weight: 300;
    text-transform: uppercase;
    line-height: 1;
  }
  .wordmark__dot {
    border-radius: 50%;
    box-sizing: border-box;
  }
  .card--front .wordmark {
    left: 104px;
    top: 126px;
    color: var(--ink-dark);
    font-size: 48px;
    letter-spacing: 6px;
  }
  .card--front .wordmark__dot {
    width: 34px;
    height: 34px;
    border: 1.5px solid var(--ink-dark);
    margin-right: 26px;
  }
  .card--back .wordmark {
    left: 40px;
    top: 126px;
    color: var(--brand-pink);
    font-size: 36px;
    letter-spacing: 4px;
  }
  .card--back .wordmark__dot {
    width: 34px;
    height: 34px;
    border: 1.5px solid var(--brand-pink);
    margin-right: 20px;
  }
  .contact {
    position: absolute;
    left: 273px;
    top: 80px;
    font-family: "Roboto", sans-serif;
    color: var(--brand-pink);
    font-size: 12px;
    line-height: 16px;
  }
  .contact__name {
    margin: 0 0 14px;
    font-family: "Advent Pro", sans-serif;
    font-weight: 600;
    font-size: 21px;
    letter-spacing: 0.8px;
    color: var(--brand-teal);
    text-transform: uppercase;
  }
  .contact__address {
    margin: 0 0 8px;
    font-style: normal;
  }
  .contact__list {
    list-style: none;
    margin: 0;
    padding: 0;
  }
  .contact__item {
    display: flex;
    align-items: center;
    height: 16.5px;
  }
  .contact__icon {
    width: 11px;
    height: 11px;
    margin-right: 11px;
    flex: none;
    fill: none;
    stroke: var(--brand-teal);
    stroke-width: 1.4;
    stroke-linecap: round;
    stroke-linejoin: round;
  }
</style>
</head>
<body>
<main class="stage">
  <section class="card card--front" aria-label="Card front">
    <div class="wordmark">
      <span class="wordmark__dot"></span>
      <span class="wordmark__name">Glowmi</span>
    </div>
  </section>

  <section class="card card--back" aria-label="Card back">
    <div class="wordmark">
      <span class="wordmark__dot"></span>
      <span class="wordmark__name">Glowmi</span>
    </div>
    <div class="contact">
      <h1 class="contact__name">Mara Ellis</h1>
      <address class="contact__address">123, Street Number, City Name,<br>Country - 123456</address>
      <ul class="contact__list">
        <li class="contact__item">
          <svg class="contact__icon" viewBox="0 0 12 12" aria-hidden="true"><path d="M2 1.5 L4 1.5 L5 4 L3.8 5 Q5 7.5 7 8.2 L8 7 L10.5 8 L10.5 10 Q6 11 3 8 Q0.8 5 2 1.5 Z"/></svg>
          <span>00 555 010 482</span>
        </li>
        <li class="contact__item">
          <svg class="contact__icon" viewBox="0 0 12 12" aria-hidden="true"><path d="M5 7 L7 5"/><path d="M6 3 L7.5 1.5 Q9 0.5 10.5 1.5 Q11.5 3 10.5 4.5 L9 6"/><path d="M6 9 L4.5 10.5 Q3 11.5 1.5 10.5 Q0.5 9 1.5 7.5 L3 6"/></svg>
          <span>www.glowmi-example.com</span>
        </li>
        <li class="contact__item">
          <svg class="contact__icon" viewBox="0 0 12 12" aria-hidden="true"><rect x="1" y="2.5" width="10" height="7"/><path d="M1 2.5 L6 6.5 L11 2.5"/></svg>
          <span>yourname@glowmi-example.com</span>
        </li>
      </ul>
    </div>
  </section>
</main>
</body>
</html>
```